Florida-based Coastal Landscaping Comapny Needs Postcard Designs

We are a newly established Florida-based, coastal landscaping company that is looking for some really innovative postcards that we can use to get our name our to affluent consumers that live on the coast of Florida (think on the beach) and small to medium sized businesses in the same area. We will be sending out 100s of thousands of these, so need a great design

Target Market(s)

Affluent consumers and small to medium sized businesses

Industry/Entity Type

Landscaping

Font styles to use
Sans Serif

Colors

Designer to choose colors to be used in the design.

Requirements
Must have
• Florida - looking, island looking / paradise, but incorporate landscaping themes
• Need to say something about "Enjoy your yard this summer" or something relating to summer, landscapes and florida
• and would like to make two offers $50.00 off with signing up for one of our routine maintenance programs, or 1 free landscape inspection
Should not have
• Regular generic lawn company designs. We are a top tier landscape design / build plus maintenance firm, so not your mom and pop lawn mowing company

```html
<!DOCTYPE html>
<html lang="en">
<head>
<meta charset="utf-8">
<title>Shore Verde – Summer Postcard</title>
<link rel="stylesheet" href="https://fonts.googleapis.com/css2?family=Marcellus+SC&family=Oswald:wght@400;500;600&family=Jost:wght@500;600&display=swap">
<style>
  :root {
    --backdrop: #2b2b2d;
    --sky-light: #f1f4f8;
    --sky-mid: #d4e2ee;
    --brand-blue: #1e9ad6;
    --deep-blue: #1b5aa6;
    --navy: #1d3f8a;
    --water-pale: #c5d7df;
    --sage: #a3b19a;
    --white: #ffffff;
    --ink: #333333;
    --stamp: #ebebeb;
  }
  * { margin: 0; padding: 0; box-sizing: border-box; }
  html, body { width: 960px; height: 1200px; overflow: hidden; }
  body { background: var(--backdrop); position: relative; }

  .card { position: absolute; overflow: hidden; }
  .card svg.art { position: absolute; inset: 0; width: 100%; height: 100%; }

  /* Front */
  .card--front {
    left: 120px; top: 32px; width: 730px; height: 562px;
    background: linear-gradient(to bottom, var(--sky-light) 0%, var(--sky-mid) 30%);
  }
  .headline {
    position: absolute; right: 38px; top: 22px;
    font-family: "Marcellus SC", "Optima", sans-serif;
    text-align: right; line-height: 1;
  }
  .headline__lead { display: block; font-size: 56px; color: var(--brand-blue); letter-spacing: 0.5px; }
  .headline__season { display: block; font-size: 62px; color: var(--deep-blue); margin-top: 4px; letter-spacing: 1px; }

  .offer { position: absolute; left: 30px; top: 428px; font-family: "Oswald", sans-serif; color: var(--deep-blue); }
  .offer__amount { position: absolute; left: 0; top: 0; font-size: 62px; font-weight: 600; line-height: 1; letter-spacing: -1px; }
  .offer__off { position: absolute; left: 58px; top: 68px; font-size: 24px; font-weight: 600; line-height: 1; }
  .offer__divider { position: absolute; left: 120px; top: 10px; height: 84px; border-left: 2px dotted var(--brand-blue); }
  .offer__terms { position: absolute; left: 133px; top: 34px; width: 320px; font-size: 18px; line-height: 23px; font-weight: 400; color: var(--deep-blue); text-transform: uppercase; }
  .offer__alt { position: absolute; left: 0; top: 100px; white-space: nowrap; font-size: 26px; font-weight: 500; text-transform: uppercase; }
  .offer__alt strong { font-weight: 600; }

  .brand { font-family: "Jost", sans-serif; font-weight: 500; color: var(--deep-blue); letter-spacing: 1px; white-space: nowrap; }
  .brand--front { position: absolute; left: 452px; top: 512px; font-size: 28px; }
  .brand--back { position: absolute; left: 386px; top: 68px; font-size: 22px; }

  /* Back */
  .card--back { left: 120px; top: 618px; width: 723px; height: 556px; background: var(--white); }
  .stamp-box { position: absolute; left: 595px; top: 26px; width: 103px; height: 103px; background: var(--stamp); }
  .contact { position: absolute; left: 54px; top: 396px; font-family: "Jost", sans-serif; color: var(--white); line-height: 1; }
  .contact__title { font-size: 40px; font-weight: 500; letter-spacing: 0.5px; }
  .contact__phone { font-size: 44px; font-weight: 600; margin-top: 10px; letter-spacing: 0.5px; }
  .contact__web { font-size: 28px; font-weight: 500; margin-top: 12px; letter-spacing: 0.5px; }
</style>
</head>
<body>

<section class="card card--front">
  <svg class="art" viewBox="0 0 730 562" preserveAspectRatio="none">
    <defs>
      <linearGradient id="villaScene" x1="0" y1="0" x2="0" y2="1">
        <stop offset="0" stop-color="#d6e3ee"/>
        <stop offset="0.25" stop-color="#b4653f"/>
        <stop offset="0.45" stop-color="#e8dccb"/>
        <stop offset="0.75" stop-color="#8a9a63"/>
        <stop offset="1" stop-color="#ecebe4"/>
      </linearGradient>
    </defs>
    <rect role="img" aria-label="Mediterranean beachfront villa with palm trees and white sand" x="0" y="168" width="730" height="300" fill="url(#villaScene)"/>
    <path d="M0 440 C110 395 230 380 380 415 C520 450 640 450 730 410 L730 562 L0 562 Z" fill="var(--water-pale)"/>
    <path d="M0 440 C110 395 230 380 380 415 C520 450 640 450 730 410 L730 404 C640 438 520 438 380 404 C230 370 110 380 0 430 Z" fill="var(--deep-blue)"/>
    <path d="M30 418 C140 378 250 372 380 404 C520 438 640 438 730 404 L730 398 C640 428 520 426 380 394 C260 366 150 370 30 418 Z" fill="var(--brand-blue)"/>
  </svg>

  <h1 class="headline">
    <span class="headline__lead">Enjoy your yard this</span>
    <span class="headline__season">Summer</span>
  </h1>

  <div class="offer">
    <span class="offer__amount">$50</span>
    <span class="offer__off">OFF</span>
    <span class="offer__divider"></span>
    <p class="offer__terms">Signing up for one of our<br>routine maintenance programs</p>
    <p class="offer__alt">or <strong>1 free irrigation inspection</strong></p>
  </div>

  <div class="brand brand--front">SHORE VERDE</div>
</section>

<section class="card card--back">
  <svg class="art" viewBox="0 0 723 556" preserveAspectRatio="none">
    <defs>
      <linearGradient id="estateScene" x1="0" y1="0" x2="0" y2="1">
        <stop offset="0" stop-color="#2f7fd6"/>
        <stop offset="0.2" stop-color="#5d9b57"/>
        <stop offset="0.42" stop-color="#e8d9a0"/>
        <stop offset="0.58" stop-color="#b7468f"/>
        <stop offset="0.72" stop-color="#6f8a55"/>
        <stop offset="1" stop-color="#a7b79a"/>
      </linearGradient>
      <clipPath id="photoEdge">
        <path d="M372 0 C330 110 300 190 330 290 C360 380 400 450 400 556 L0 556 L0 0 Z"/>
      </clipPath>
    </defs>
    <path d="M384 0 C342 110 312 190 342 290 C372 380 412 450 412 556 L400 556 C400 450 360 380 330 290 C300 190 330 110 372 0 Z" fill="var(--brand-blue)"/>
    <path d="M392 0 C350 110 320 190 350 290 C380 380 420 450 420 556 L412 556 C412 450 372 380 342 290 C312 190 342 110 384 0 Z" fill="var(--deep-blue)"/>
    <g clip-path="url(#photoEdge)">
      <rect role="img" aria-label="Waterfront estate with verandas and flowering bougainvillea beside a lagoon" x="0" y="0" width="420" height="556" fill="url(#estateScene)"/>
      <rect x="0" y="374" width="420" height="182" fill="var(--sage)"/>
    </g>
  </svg>

  <div class="brand brand--back">SHORE VERDE</div>
  <div class="stamp-box"></div>

  <div class="contact">
    <p class="contact__title">CONTACT US</p>
    <p class="contact__phone">123-456-789</p>
    <p class="contact__web">www.website.com</p>
  </div>
</section>

</body>
</html>
```